Quorvane Capital Modern Business Card

We need a modern business card template designed for Quorvane Capital.
Quorvane Capital is a diversified global cryptocurrency investment fund.

The font under the logo: Hiragino Kaku Gothic Pro

Color Hexcode: Main colors white (ffffff) & teal (188383), we are open to adding #fcca46 as an accent

Target Market(s)

Accredited Investors, high net worth individuals and institutional investors

Industry/Entity Type

Investment

Contact Information for Business Card

Contact Information should contain
Name
main phone +1 720 555 0147
cell
email

Font styles to use
Sans Serif
Other font styles liked:
• Hiragino Kaku Gothic Pro

Requirements
Must have
• would like to have icons that identify the contact information
• include our website: www.quorvanecapital.example
• include our Tagline: Diversified Crypto Investment Funds
Nice to have
• Would like to have a simple back side with the logo (without the words) and plenty of space

```html
<!DOCTYPE html>
<html lang="en">
<head>
<meta charset="utf-8">
<title>Quorvane Capital Stationery</title>
<link rel="stylesheet" href="https://fonts.googleapis.com/css2?family=Arimo:wght@400;500&family=Noto+Sans+JP:wght@400;500&display=swap">
<style>
  :root {
    --teal: #188383;
    --paper: #e6e6e6;
    --stage: #c8c8c8;
    --ink: #1a1a1a;
    --grey-text: #8a8a8a;
    --grey-block: #8f8f8f;
    --white: #ffffff;
  }
  * { box-sizing: border-box; margin: 0; padding: 0; }
  html, body { width: 1200px; height: 890px; overflow: hidden; }
  body {
    background: var(--stage);
    font-family: "Arimo", "Helvetica Neue", Arial, sans-serif;
    position: relative;
  }
  .brand-name { font-family: "Noto Sans JP", "Arimo", sans-serif; }

  /* Letterhead */
  .letterhead {
    position: absolute; left: 52px; top: 74px; width: 579px; height: 741px;
    background: var(--paper);
  }
  .letterhead .brand-name {
    position: absolute; top: 94px; left: 0; width: 100%;
    text-align: center; font-size: 13px; color: var(--ink); letter-spacing: 0.2px;
  }
  .meta-label { font-size: 9.5px; font-weight: 500; color: var(--ink); }
  .meta-value { font-size: 9px; color: var(--grey-text); margin-top: 2px; }
  .subject { position: absolute; left: 147px; top: 206px; }
  .date { position: absolute; left: 453px; top: 206px; }
  .salutation {
    position: absolute; left: 147px; top: 283px;
    font-size: 12.5px; color: #6f6f6f;
  }
  .side-notes {
    position: absolute; left: 10px; top: 312px; width: 120px;
    text-align: right; font-size: 8.8px; line-height: 12.4px; color: var(--grey-text);
  }
  .side-notes p { margin-bottom: 6px; }
  .side-notes strong { font-weight: 400; color: var(--ink); }
  .letter-body {
    position: absolute; left: 147px; top: 312px; width: 354px;
    font-size: 8.8px; line-height: 12.4px; color: var(--grey-text); text-align: justify;
  }
  .letter-body p { margin-bottom: 12.4px; }
  .signature {
    position: absolute; left: 147px; top: 588px;
    font-size: 12px; line-height: 15px; color: #6f6f6f;
  }
  .letter-footer {
    position: absolute; left: 0; top: 669px; width: 579px; height: 57px;
    background: var(--teal); overflow: hidden;
  }
  .letter-footer .contact-list { position: absolute; left: 22px; top: 6px; }
  .letter-footer .contact-list li { font-size: 9px; line-height: 12px; }
  .letter-footer .corner { position: absolute; left: 0; top: 0; }

  /* Contact list shared */
  .contact-list { list-style: none; color: var(--white); }
  .contact-list li { display: flex; align-items: center; gap: 5px; white-space: nowrap; }
  .contact-list svg { flex: none; }

  /* Business card front */
  .card-front {
    position: absolute; left: 681px; top: 157px; width: 452px; height: 261px;
    background: var(--paper); overflow: hidden;
  }
  .card-front .brand-name {
    position: absolute; left: 21px; top: 90px; font-size: 11.5px; color: var(--ink);
  }
  .card-front .pointer { position: absolute; left: 0; top: 125px; }
  .holder-name {
    position: absolute; left: 21px; top: 123px;
    font-size: 14.5px; color: var(--teal); letter-spacing: 0.4px;
  }
  .holder-role {
    position: absolute; left: 21px; top: 142px; font-size: 10px; color: var(--grey-text);
  }
  .card-band {
    position: absolute; left: 0; top: 167px; width: 452px; height: 71px;
    background: var(--teal); overflow: hidden;
  }
  .card-band .contact-list { position: absolute; left: 21px; top: 6px; }
  .card-band .contact-list li { font-size: 11px; line-height: 14.6px; }
  .card-band .corner { position: absolute; left: 0; top: 0; }
  .tagline {
    position: absolute; left: 21px; top: 243px; font-size: 11px; color: var(--teal);
  }

  /* Business card back */
  .card-back {
    position: absolute; left: 681px; top: 470px; width: 453px; height: 262px;
    background: var(--teal);
    display: flex; align-items: center; justify-content: center; gap: 10px;
  }
  .card-back .mark-dot { width: 12px; height: 12px; background: var(--paper); }
  .card-back .brand-name { font-size: 20px; color: var(--paper); letter-spacing: 1px; }
</style>
</head>
<body>

<section class="letterhead">
  <div class="brand-name">QUORVANE CAPITAL</div>

  <div class="subject">
    <div class="meta-label">SUBJECT :</div>
    <div class="meta-value">Lorem Ipsum is simply dummy</div>
  </div>
  <div class="date">
    <div class="meta-label">DATE :</div>
    <div class="meta-value">15-09-2017</div>
  </div>

  <div class="salutation">Dear Person,</div>

  <aside class="side-notes">
    <p><strong>Lorem Ipsum is</strong><br>simply dummy text<br>of the printing</p>
    <p><strong>Lorem Ipsum is</strong><br>simply dummy text</p>
  </aside>

  <div class="letter-body">
    <p>Lorem Ipsum is simply dummy text of the printing and typesetting industry. Lorem Ipsum has been the industry's standard dummy text ever since the 1500s, when an unknown printer took a galley of type and scrambled it to make a type specimen book. It has survived not only five centuries, but also the leap into electronic typesetting, remaining essentially unchanged. It was popularised in the 1960s with the release of Letraset sheets containing Lorem Ipsum passages, and more recently with desktop publishing software like Aldus PageMaker including versions of Lorem Ipsum.</p>
    <p>Lorem Ipsum is simply dummy text of the printing and typesetting industry. Lorem Ipsum has been the industry's standard dummy text ever since the 1500s, when an unknown printer took a galley of type and scrambled it to make a type specimen book. It has survived not only five centuries, but also the leap into electronic typesetting, remaining essentially unchanged. It was popularised in the 1960s with the release of</p>
    <p>Letraset sheets containing Lorem Ipsum passages, and more recently with desktop publishing software like Aldus PageMaker including versions of Lorem Ipsum.lease of Letraset sheets containing Lorem Ipsum passages, and more recently with desktop publishing software like Aldus PageMaker including versions of Lorem Ipsum. publishing software like Aldus PageMaker including versions of Lorem Ipsum.</p>
  </div>

  <div class="signature">Martin Hollis<br>Managing Director</div>

  <footer class="letter-footer">
    <svg class="corner" width="579" height="57" aria-hidden="true">
      <polygon points="502,0 579,0 579,57 534,57" fill="var(--grey-block)"/>
    </svg>
    <ul class="contact-list">
      <li><svg width="9" height="9" viewBox="0 0 10 10"><circle cx="5" cy="5" r="5" fill="#fff" opacity=".85"/><rect x="3.2" y="2" width="3.6" height="6" rx=".6" fill="var(--teal)"/></svg>+1 720 555 0147</li>
      <li><svg width="9" height="9" viewBox="0 0 10 10"><circle cx="5" cy="5" r="5" fill="#fff" opacity=".85"/><path d="M3 2.5 L4.2 2.3 L4.8 3.8 L4.1 4.4 Q4.8 5.6 5.8 6.1 L6.4 5.4 L7.8 6 L7.6 7.3 Q4.5 7.6 3 2.5Z" fill="var(--teal)"/></svg>+1 303 555 0192</li>
      <li><svg width="9" height="9" viewBox="0 0 10 10"><circle cx="5" cy="5" r="5" fill="#fff" opacity=".85"/><rect x="2.4" y="3.2" width="5.2" height="3.6" fill="none" stroke="var(--teal)" stroke-width=".8"/><path d="M2.4 3.2 L5 5.2 L7.6 3.2" fill="none" stroke="var(--teal)" stroke-width=".8"/></svg>info@quorvanecapital.example</li>
      <li><svg width="9" height="9" viewBox="0 0 10 10"><circle cx="5" cy="5" r="5" fill="#fff" opacity=".85"/><circle cx="5" cy="5" r="2.8" fill="none" stroke="var(--teal)" stroke-width=".7"/><path d="M2.2 5 H7.8 M5 2.2 V7.8" stroke="var(--teal)" stroke-width=".7"/></svg>www.quorvanecapital.example</li>
    </ul>
  </footer>
</section>

<section class="card-front">
  <div class="brand-name">QUORVANE CAPITAL</div>
  <svg class="pointer" width="14" height="30" aria-hidden="true"><polygon points="0,0 14,15 0,30" fill="var(--teal)"/></svg>
  <div class="holder-name">DARREN OKAFOR</div>
  <div class="holder-role">Co-Founder</div>

  <div class="card-band">
    <svg class="corner" width="452" height="71" aria-hidden="true">
      <polygon points="359,0 452,0 452,71 401,71" fill="var(--grey-block)"/>
    </svg>
    <ul class="contact-list">
      <li><svg width="11" height="11" viewBox="0 0 10 10"><circle cx="5" cy="5" r="5" fill="#fff" opacity=".85"/><rect x="3.2" y="2" width="3.6" height="6" rx=".6" fill="var(--teal)"/></svg>+1 720 555 0147</li>
      <li><svg width="11" height="11" viewBox="0 0 10 10"><circle cx="5" cy="5" r="5" fill="#fff" opacity=".85"/><path d="M3 2.5 L4.2 2.3 L4.8 3.8 L4.1 4.4 Q4.8 5.6 5.8 6.1 L6.4 5.4 L7.8 6 L7.6 7.3 Q4.5 7.6 3 2.5Z" fill="var(--teal)"/></svg>+1 303 555 0192</li>
      <li><svg width="11" height="11" viewBox="0 0 10 10"><circle cx="5" cy="5" r="5" fill="#fff" opacity=".85"/><rect x="2.4" y="3.2" width="5.2" height="3.6" fill="none" stroke="var(--teal)" stroke-width=".8"/><path d="M2.4 3.2 L5 5.2 L7.6 3.2" fill="none" stroke="var(--teal)" stroke-width=".8"/></svg>info@quorvanecapital.example</li>
      <li><svg width="11" height="11" viewBox="0 0 10 10"><circle cx="5" cy="5" r="5" fill="#fff" opacity=".85"/><circle cx="5" cy="5" r="2.8" fill="none" stroke="var(--teal)" stroke-width=".7"/><path d="M2.2 5 H7.8 M5 2.2 V7.8" stroke="var(--teal)" stroke-width=".7"/></svg>www.quorvanecapital.example</li>
    </ul>
  </div>

  <div class="tagline">Diversified Crypto Investment Funds</div>
</section>

<section class="card-back">
  <span class="mark-dot" aria-hidden="true"></span>
  <span class="brand-name">QUORVANE CAPITAL</span>
</section>

</body>
</html>
```